Brindle Works Ltd

I'd like to create a company letterhead for the attached logo in word format.

I'd like to emphasis the icon in large translucent state from the left corner and ensure that the letterhead colouring matches the colour palette of the current logo with a contrast so it's clear to see. I've attached a copy of our sister company page on the app for reference.

```html
<!DOCTYPE html>
<html lang="en">
<head>
<meta charset="utf-8">
<title>Brindle Works Ltd Letterhead</title>
<link href="https://fonts.googleapis.com/css2?family=Lato:wght@400;700&family=Italianno&display=swap" rel="stylesheet">
<style>
  :root {
    --teal: #17b8a0;
    --teal-faint: #e2f2ee;
    --ink: #1c1c1c;
    --grey: #6b6b6b;
    --paper: #ffffff;
  }
  * { margin: 0; padding: 0; box-sizing: border-box; }
  html, body { width: 1040px; height: 1200px; overflow: hidden; background: var(--paper); }
  .letterhead {
    position: relative;
    width: 1040px; height: 1200px;
    font-family: "Lato", Arial, sans-serif;
    color: var(--ink);
  }
  .backdrop-disc {
    position: absolute;
    left: 250px; top: 300px;
    width: 530px; height: 530px;
    border-radius: 50%;
    background: var(--teal-faint);
    opacity: 0.55;
  }
  .brand {
    position: absolute;
    left: 52px; top: 150px;
    display: flex; align-items: center; gap: 14px;
  }
  .brand-dot {
    width: 30px; height: 30px; border-radius: 50%;
    background: var(--teal);
  }
  .brand-name {
    font-family: "Lato", Arial, sans-serif;
    font-weight: 700; font-size: 38px;
    color: var(--teal); letter-spacing: 0.5px;
  }
  .contact {
    position: absolute;
    left: 708px; top: 100px;
    border-left: 2px solid var(--teal);
    padding-left: 20px;
    font-size: 17px; line-height: 22px;
  }
  .contact .address { margin-bottom: 12px; }
  .contact-line { display: flex; align-items: center; gap: 6px; }
  .contact-line svg { width: 11px; height: 11px; fill: var(--teal); }
  .letter {
    position: absolute;
    left: 52px; top: 325px;
    width: 923px;
    font-size: 20px; line-height: 23px;
  }
  .date { margin-bottom: 22px; }
  .recipient { margin-bottom: 20px; }
  .address-block { margin-bottom: 26px; }
  .salutation { font-weight: 700; font-size: 25px; margin-bottom: 24px; }
  .body p { text-align: justify; margin-bottom: 22px; }
  .closing { margin-top: 36px; }
  .signature {
    font-family: "Italianno", cursive;
    font-size: 52px; margin-top: 46px; line-height: 1;
  }
</style>
</head>
<body>
<main class="letterhead">
  <div class="backdrop-disc" aria-hidden="true"></div>

  <header>
    <div class="brand">
      <span class="brand-dot"></span>
      <span class="brand-name">Brindle Works Ltd</span>
    </div>
    <address class="contact" style="font-style:normal">
      <div class="address">418 Harlow Ave, Suite 12<br>Millbrook, OR 97401</div>
      <div class="contact-line">
        <svg viewBox="0 0 24 24"><path d="M6.6 10.8a15.1 15.1 0 0 0 6.6 6.6l2.2-2.2a1 1 0 0 1 1-.25 11.4 11.4 0 0 0 3.6.57 1 1 0 0 1 1 1V20a1 1 0 0 1-1 1A17 17 0 0 1 3 4a1 1 0 0 1 1-1h3.5a1 1 0 0 1 1 1c0 1.25.2 2.45.57 3.57a1 1 0 0 1-.25 1z"/></svg>
        <span>(541) 208-6634</span>
      </div>
      <div class="contact-line">
        <svg viewBox="0 0 24 24"><path d="M2 5h20v14H2z M2 5l10 8 10-8" /></svg>
        <span>hello@brindleworks.co</span>
      </div>
      <div class="contact-line">
        <svg viewBox="0 0 24 24"><circle cx="12" cy="12" r="10"/></svg>
        <span>www.brindleworks.co</span>
      </div>
    </address>
  </header>

  <article class="letter">
    <p class="date">January-03-2020</p>
    <p class="recipient">Mr, Alan Crest<br>President</p>
    <p class="address-block">Halvern Group<br>123 Street Name, Suite# 10<br>City, State, 120023</p>
    <h1 class="salutation">Dear Mr, Alan</h1>
    <div class="body">
      <p>Lorem ipsum dolor sit amet, consectetur adipiscing elit, sed do eiusmod tempor incididunt ut labore et dolore magna aliqua. Ut enim ad minim veniam, quis nostrud exercitation ullamco laboris nisi ut aliquip ex ea commodo consequat. Duis aute irure dolor in reprehenderit in voluptate velit esse cillum dolore eu fugiat nulla pariatur.</p>
      <p>Lorem ipsum dolor sit amet, consectetur adipiscing elit, sed do eiusmod tempor incididunt ut labore et dolore magna aliqua. Ut enim ad minim veniam, quis nostrud exercitation ullamco laboris nisi ut aliquip ex ea commodo consequat. Duis aute irure dolor in reprehenderit in voluptate velit esse cillum dolore eu fugiat nulla pariatur.</p>
      <p>Lorem ipsum dolor sit amet, consectetur adipiscing elit, sed do eiusmod tempor incididunt ut labore et dolore magna aliqua. Ut enim ad minim veniam, quis nostrud exercitation ullamco laboris nisi ut aliquip ex ea commodo consequat.</p>
      <p>Excepteur sint occaecat cupidatat non proident, sunt in culpa qui officia deserunt mollit anim id est laborum. re et dolore magnam aliquam quaerat voluptatem.</p>
    </div>
    <p class="closing">Regards</p>
    <p class="signature">Daniel Frost</p>
  </article>
</main>
</body>
</html>
```